Papaw soap display box and soap label

We need a packaging design for a Papaw (fruit) soap counter display (cardboard ) which holds 24 soaps. we also need a label for the individual soap. we have already sold similar soaps (goats milk -mainly green colour and lemon myrtle -mainly yellow) in the same display. The new Papaw should compliment these other 2 designs. the design should relect a natural healing theme The brand name is Brindle Creek Pawfruit soap
Updates

As the other 2 designs i have prsently areĀ  yellow and green backgrounds, i would prefer a different background colour for this project

Target Market(s)

more feminine 40+

Requirements
Must have
• the display box must have the following on the rear
Distributed by Kestrona Pty limited
Australian Owned
17-19 Marlow Rd Tenby NSW 2381 Australia
www.kestrona-example.com.au
barcode 9300000000017
KR750
Made in Australia

the display box must have AUSTRALIAN MADE on the front

the display box the top flap must have
-phosphate free SLS free
-by Marvique
-Brindle Creek Pawfruit Soap
- a gentle natural soap which does not dry the skin's protective barrier

the label must have
-Brindle Creek Pawfruit Soap
-phosphate free SLS free
-by Marvique
-90 gm
-Made in Australia
-barcode - 9300000000017
- Kestrona Pty limited
17-19 Marlow Rd Tenby NSW 2381
Australia
www.kestrona-example.com.au
Soap Label Size - The top section of the soap (maybe where the logo and branding is placed) is 65mm wide x 40mm.
the total label is 65mm wide and 80 long- it will wrap around the sides.the sides are approx 20mm x 65 wide x 2 sides.
these sides would best for the barcode and other written information
Nice to have
• a 'natural' look
Should not have
• claims that indicate that the soap can heal etc

```html
<!DOCTYPE html>
<html lang="en">
<head>
<meta charset="utf-8">
<title>Brindle Creek Soap Display Range</title>
<link rel="stylesheet" href="https://fonts.googleapis.com/css2?family=Oswald:wght@600&family=Pinyon+Script&family=IM+Fell+English:ital@1&display=swap">
<style>
  :root {
    --teal: #1f9d98;
    --lemon: #fbc630;
    --papaw: #f6a65b;
    --cream: #f4eee4;
    --soap-shade: #e4ddd2;
    --ink-light: #ffffff;
    --art-teal: #17807b;
    --art-lemon: #d9a620;
    --art-papaw: #c9743a;
    --page: #ffffff;
  }
  html, body { margin: 0; padding: 0; }
  body {
    width: 1200px; height: 476px; overflow: hidden;
    background: var(--page); position: relative;
  }
  .display-box { position: absolute; top: 18px; width: 292px; height: 440px; }
  .display-box--goats { left: 16px; }
  .display-box--lemon { left: 324px; }
  .display-box--papaw { left: 652px; }
  .soap-label { position: absolute; }
  .soap-label--top { left: 980px; top: 82px; width: 196px; height: 100px; }
  .soap-label--wrap { left: 1038px; top: 236px; width: 100px; height: 206px; }
  svg { display: block; }
  .fill-teal { fill: var(--teal); }
  .fill-lemon { fill: var(--lemon); }
  .fill-papaw { fill: var(--papaw); }
  .fill-cream { fill: var(--cream); }
  .fill-shade { fill: var(--soap-shade); }
  .art-teal { fill: var(--art-teal); }
  .art-lemon { fill: var(--art-lemon); }
  .art-papaw { fill: var(--art-papaw); }
  .rule { stroke: var(--ink-light); stroke-width: 1; fill: none; }
  .claim { font-family: "Oswald", sans-serif; font-weight: 600; fill: var(--ink-light); letter-spacing: .2px; }
  .brand { font-family: "Pinyon Script", cursive; fill: var(--ink-light); }
  .product { font-family: "Oswald", sans-serif; font-weight: 600; fill: var(--ink-light); letter-spacing: .4px; }
  .blurb { font-family: "IM Fell English", serif; font-style: italic; fill: var(--ink-light); }
  .made { font-family: "Oswald", sans-serif; font-weight: 600; fill: var(--ink-light); letter-spacing: .5px; }
</style>
</head>
<body>

<!-- Goats milk display -->
<div class="display-box display-box--goats">
  <svg width="292" height="440" viewBox="0 0 292 440">
    <rect class="fill-cream" x="6" y="216" width="280" height="224"/>
    <g class="fill-shade"><rect x="14" y="300" width="128" height="60" rx="3"/><rect x="150" y="300" width="128" height="60" rx="3"/></g>
    <path class="fill-teal" d="M0 62 L80 62 L80 46 A66 44 0 0 1 212 46 L212 62 L292 62 L292 216 L0 216 Z"/>
    <text class="claim" x="146" y="22" font-size="6.5" text-anchor="middle">PHOSPHATE FREE&#160;&#160;SLS FREE SOAP</text>
    <rect class="art-teal" x="122" y="27" width="48" height="33" rx="14" role="img" aria-label="Engraved goat head illustration"/>
    <path class="rule" d="M10 78 V206 M14 78 V206 M278 78 V206 M282 78 V206"/>
    <text class="brand" x="128" y="108" font-size="30" text-anchor="middle">Brindle</text>
    <text class="brand" x="160" y="132" font-size="30" text-anchor="middle">Creek</text>
    <text class="product" x="146" y="156" font-size="15" text-anchor="middle">GOATS MILK SOAP</text>
    <text class="blurb" x="146" y="182" font-size="8.6" text-anchor="middle">A gentle natural soap which does not dry the</text>
    <text class="blurb" x="146" y="194" font-size="8.6" text-anchor="middle">skin or compromise the skins protective barrier.</text>
    <g class="fill-teal">
      <rect x="18" y="222" width="120" height="14"/><rect x="154" y="222" width="120" height="14"/>
      <rect x="18" y="240" width="120" height="14"/><rect x="154" y="240" width="120" height="14"/>
      <rect x="18" y="258" width="120" height="14"/><rect x="154" y="258" width="120" height="14"/>
      <rect x="18" y="276" width="120" height="14"/><rect x="154" y="276" width="120" height="14"/>
    </g>
    <g class="product" font-size="5.5">
      <text x="134" y="231.5" text-anchor="end">GOATS MILK SOAP</text><text x="270" y="231.5" text-anchor="end">GOATS MILK SOAP</text>
      <text x="134" y="249.5" text-anchor="end">GOATS MILK SOAP</text><text x="270" y="249.5" text-anchor="end">GOATS MILK SOAP</text>
      <text x="134" y="267.5" text-anchor="end">GOATS MILK SOAP</text><text x="270" y="267.5" text-anchor="end">GOATS MILK SOAP</text>
      <text x="134" y="285.5" text-anchor="end">GOATS MILK SOAP</text><text x="270" y="285.5" text-anchor="end">GOATS MILK SOAP</text>
    </g>
    <g class="brand" font-size="7.5">
      <text x="23" y="232">Brindle Creek</text><text x="159" y="232">Brindle Creek</text>
      <text x="23" y="250">Brindle Creek</text><text x="159" y="250">Brindle Creek</text>
      <text x="23" y="268">Brindle Creek</text><text x="159" y="268">Brindle Creek</text>
      <text x="23" y="286">Brindle Creek</text><text x="159" y="286">Brindle Creek</text>
    </g>
    <path class="fill-teal" d="M0 216 L10 216 Q18 330 52 380 L240 380 Q274 330 282 216 L292 216 L292 440 L0 440 Z"/>
    <path class="rule" d="M6 240 V370 M10 240 Q14 330 36 372 M286 240 V370 M282 240 Q278 330 256 372"/>
    <text class="made" x="146" y="428" font-size="24" text-anchor="middle">AUSTRALIAN MADE</text>
  </svg>
</div>

<!-- Lemon myrtle display -->
<div class="display-box display-box--lemon">
  <svg width="292" height="440" viewBox="0 0 292 440">
    <rect class="fill-cream" x="6" y="216" width="280" height="224"/>
    <g class="fill-shade"><rect x="14" y="300" width="128" height="60" rx="3"/><rect x="150" y="300" width="128" height="60" rx="3"/></g>
    <path class="fill-lemon" d="M0 62 L80 62 L80 46 A66 44 0 0 1 212 46 L212 62 L292 62 L292 216 L0 216 Z"/>
    <text class="claim" x="146" y="22" font-size="6.5" text-anchor="middle">PHOSPHATE FREE&#160;&#160;SLS FREE SOAP</text>
    <rect class="art-lemon" x="122" y="27" width="48" height="33" rx="14" role="img" aria-label="Engraved lemon myrtle sprig illustration"/>
    <path class="rule" d="M10 78 V206 M14 78 V206 M278 78 V206 M282 78 V206"/>
    <text class="brand" x="128" y="108" font-size="30" text-anchor="middle">Brindle</text>
    <text class="brand" x="160" y="132" font-size="30" text-anchor="middle">Creek</text>
    <text class="product" x="146" y="156" font-size="15" text-anchor="middle">LEMON MYRTLE SOAP</text>
    <text class="blurb" x="146" y="182" font-size="8.6" text-anchor="middle">A gentle natural soap which does not dry the</text>
    <text class="blurb" x="146" y="194" font-size="8.6" text-anchor="middle">skin or compromise the skins protective barrier.</text>
    <g class="fill-lemon">
      <rect x="18" y="222" width="120" height="14"/><rect x="154" y="222" width="120" height="14"/>
      <rect x="18" y="240" width="120" height="14"/><rect x="154" y="240" width="120" height="14"/>
      <rect x="18" y="258" width="120" height="14"/><rect x="154" y="258" width="120" height="14"/>
      <rect x="18" y="276" width="120" height="14"/><rect x="154" y="276" width="120" height="14"/>
    </g>
    <g class="product" font-size="5.5">
      <text x="134" y="231.5" text-anchor="end">LEMON MYRTLE SOAP</text><text x="270" y="231.5" text-anchor="end">LEMON MYRTLE SOAP</text>
      <text x="134" y="249.5" text-anchor="end">LEMON MYRTLE SOAP</text><text x="270" y="249.5" text-anchor="end">LEMON MYRTLE SOAP</text>
      <text x="134" y="267.5" text-anchor="end">LEMON MYRTLE SOAP</text><text x="270" y="267.5" text-anchor="end">LEMON MYRTLE SOAP</text>
      <text x="134" y="285.5" text-anchor="end">LEMON MYRTLE SOAP</text><text x="270" y="285.5" text-anchor="end">LEMON MYRTLE SOAP</text>
    </g>
    <g class="brand" font-size="7.5">
      <text x="23" y="232">Brindle Creek</text><text x="159" y="232">Brindle Creek</text>
      <text x="23" y="250">Brindle Creek</text><text x="159" y="250">Brindle Creek</text>
      <text x="23" y="268">Brindle Creek</text><text x="159" y="268">Brindle Creek</text>
      <text x="23" y="286">Brindle Creek</text><text x="159" y="286">Brindle Creek</text>
    </g>
    <path class="fill-lemon" d="M0 216 L10 216 Q18 330 52 380 L240 380 Q274 330 282 216 L292 216 L292 440 L0 440 Z"/>
    <path class="rule" d="M6 240 V370 M10 240 Q14 330 36 372 M286 240 V370 M282 240 Q278 330 256 372"/>
    <text class="made" x="146" y="428" font-size="24" text-anchor="middle">AUSTRALIAN MADE</text>
  </svg>
</div>

<!-- Pawfruit display -->
<div class="display-box display-box--papaw">
  <svg width="292" height="440" viewBox="0 0 292 440">
    <rect class="fill-cream" x="6" y="216" width="280" height="224"/>
    <g class="fill-shade"><rect x="14" y="300" width="128" height="60" rx="3"/><rect x="150" y="300" width="128" height="60" rx="3"/></g>
    <path class="fill-papaw" d="M0 62 L80 62 L80 46 A66 44 0 0 1 212 46 L212 62 L292 62 L292 216 L0 216 Z"/>
    <text class="claim" x="146" y="22" font-size="6.5" text-anchor="middle">PHOSPHATE FREE&#160;&#160;SLS FREE SOAP</text>
    <rect class="art-papaw" x="110" y="27" width="72" height="33" rx="14" role="img" aria-label="Papaw fruit halves illustration"/>
    <path class="rule" d="M10 78 V206 M14 78 V206 M278 78 V206 M282 78 V206"/>
    <text class="brand" x="128" y="108" font-size="30" text-anchor="middle">Brindle</text>
    <text class="brand" x="160" y="132" font-size="30" text-anchor="middle">Creek</text>
    <text class="product" x="146" y="156" font-size="15" text-anchor="middle">PAWFRUIT SOAP</text>
    <text class="blurb" x="146" y="182" font-size="8.6" text-anchor="middle">A gentle natural soap which does not dry the</text>
    <text class="blurb" x="146" y="194" font-size="8.6" text-anchor="middle">skin or compromise the skins protective barrier.</text>
    <g class="fill-papaw">
      <rect x="18" y="222" width="120" height="14"/><rect x="154" y="222" width="120" height="14"/>
      <rect x="18" y="240" width="120" height="14"/><rect x="154" y="240" width="120" height="14"/>
      <rect x="18" y="258" width="120" height="14"/><rect x="154" y="258" width="120" height="14"/>
      <rect x="18" y="276" width="120" height="14"/><rect x="154" y="276" width="120" height="14"/>
    </g>
    <g class="product" font-size="5.5">
      <text x="134" y="231.5" text-anchor="end">PAWFRUIT SOAP</text><text x="270" y="231.5" text-anchor="end">PAWFRUIT SOAP</text>
      <text x="134" y="249.5" text-anchor="end">PAWFRUIT SOAP</text><text x="270" y="249.5" text-anchor="end">PAWFRUIT SOAP</text>
      <text x="134" y="267.5" text-anchor="end">PAWFRUIT SOAP</text><text x="270" y="267.5" text-anchor="end">PAWFRUIT SOAP</text>
      <text x="134" y="285.5" text-anchor="end">PAWFRUIT SOAP</text><text x="270" y="285.5" text-anchor="end">PAWFRUIT SOAP</text>
    </g>
    <g class="brand" font-size="7.5">
      <text x="23" y="232">Brindle Creek</text><text x="159" y="232">Brindle Creek</text>
      <text x="23" y="250">Brindle Creek</text><text x="159" y="250">Brindle Creek</text>
      <text x="23" y="268">Brindle Creek</text><text x="159" y="268">Brindle Creek</text>
      <text x="23" y="286">Brindle Creek</text><text x="159" y="286">Brindle Creek</text>
    </g>
    <path class="fill-papaw" d="M0 216 L10 216 Q18 330 52 380 L240 380 Q274 330 282 216 L292 216 L292 440 L0 440 Z"/>
    <path class="rule" d="M6 240 V370 M10 240 Q14 330 36 372 M286 240 V370 M282 240 Q278 330 256 372"/>
    <text class="made" x="146" y="428" font-size="24" text-anchor="middle">AUSTRALIAN MADE</text>
  </svg>
</div>

<!-- Soap label, top panel -->
<div class="soap-label soap-label--top">
  <svg width="196" height="100" viewBox="0 0 196 100">
    <rect class="fill-papaw" width="196" height="100"/>
    <rect class="art-papaw" x="8" y="30" width="76" height="44" rx="16" role="img" aria-label="Papaw fruit halves illustration"/>
    <text class="brand" x="124" y="38" font-size="22" text-anchor="middle">Brindle</text>
    <text class="brand" x="150" y="58" font-size="22" text-anchor="middle">Creek</text>
    <text class="product" x="140" y="78" font-size="12" text-anchor="middle">PAWFRUIT SOAP</text>
  </svg>
</div>

<!-- Soap label, wrap view -->
<div class="soap-label soap-label--wrap">
  <svg width="100" height="206" viewBox="0 0 100 206">
    <rect class="fill-papaw" width="100" height="206"/>
    <text class="claim" x="50" y="14" font-size="6" text-anchor="middle">PHOSPHATE FREE&#160;SLS FREE</text>
    <rect class="art-papaw" x="18" y="24" width="64" height="44" rx="16" role="img" aria-label="Papaw fruit halves illustration"/>
    <text class="brand" x="44" y="118" font-size="20" text-anchor="middle">Brindle</text>
    <text class="brand" x="60" y="138" font-size="20" text-anchor="middle">Creek</text>
    <text class="product" x="50" y="156" font-size="10" text-anchor="middle">PAWFRUIT SOAP</text>
    <path class="rule" d="M10 184 H90 M10 188 H90"/>
  </svg>
</div>

</body>
</html>
```